vermalo web design

- Company / Site Description
We are developing a website that will allow anyone in Europe to find in one click, cultural things to do (Exhibition, Museum, Monument, Zoo, Aquarium, Archaeological site…) with friends or family, and to organize the visit (book a ticket / a private visit, book a restaurant nearby…).

Examples
1. You're in London with your girlfriend, it's saturday 10 am, you have two hours to spend and you want to see an exhibition. We provide you in one click all the exhibition matching your location / time and date.

2. You're in Berlin with some friends, it's thursday night you want to go out, but you don't know what to do. We provide you a list of experience, you can select for instance "I want to be on top of the world", and we show you a list of venues matching the selected experience / date / time /location of your request.

- Brand name : Vermalo
- Activity : Cultural Leisure, cultural entertainment

- Target audience
Broad target will be between 20 and 55. Core target will be between 25 and 40. Most likely to live in a city and in Europe.

- Behaviours and preferences
Our user is under time constraint (few minutes to find and choose his visit), idea constraint (is not sure about what to do and see) and money constraint.
He wants to have an easy to use website, not cluttered with information, focussed on added value information. He wants to have a website which is modern, fun and elegant that he will deem as professional and trustworthy.

- Our expectations (Do’s and Don’t)
We want to move away from traditional design. We want some OUT OF THE BOX design. Think of a website design that will look like an app design.
We want to make an awesome / extra ordinary /remember-able design. The design must be so cool, that the user wants to come back to the site. In two words: THINK EXTRAORDINARY.
You can use photos to help the user understand functions. If you use photo, use creative commons license photo.
Avoid black colors

- Functional Requirements
We need Four pages:
1. Home Page (desktop and mobile version): it’s both the homepage and the assistant page. This page will allow the user to find in one click his visit (please refer to the pdf file Assistant home page). The page must be self-explanatory for a first time user.
2. Assistant result page (desktop version): it’s the page that display the results found by the assistant based on the criteria search (please refer to the pdf file mockup - Assistant result page)
3. Site / Event page (desktop version): it’s the page that display each result information (please refer to the pdf file mockup – Event / Site Page)
The pdf files list all the elements include in each page + gives you a mockup of each page (just to put in perspective the element required). You are completely free about the design.
We don’t have the logo yet. Use a dummy logo for your page design.
The selected winner can expect to work with us immediately after the contest and on a on a regular basis later on.

- Technical Requirements
No Flash
For the winner, we will manage the CSS you will just need to provide :
. One PSD file containing all the pages
. Inside the PSD file we want for each page two groups: the first group will embed the desktop design, the second group will embed the responsive mobile design (Home Page only).
In total there should be 4 groups inside the PSD file (3 desktop groups, 1 mobile group).
Each group must contain all the elements specified in the pdf file

Website we like
http://demo.plandorix.example/?theme=Velunt
http://rosabel.quintorhub.example/#home
http://blogsite.fenk.daltoroute.example/2/
http://demo.plandorix.example/?theme=Mosaru
http://www.quarnivo.example/themes/lumbe/
http://gridmarket.example/item/tav-responsive-photography-blog-theme/full_screen_preview/8146027
http://items.zkvortel.example/?product=example
http://uk.harnoway.example

Reason: Due to the request of several designers, we have agreed to add 7 additional days to the contest deadline. Thank you. The vermalo team

Reason: We still need to collect all the votes. Sorry for the delay.

Reason: Hello, We extend the contest deadline, in order to collect all the votes from the poll. We should have everything finalized by sunday. Thank you vermalo team

```html
<!DOCTYPE html>
<html lang="en">
<head>
<meta charset="utf-8">
<title>Vermalo — MyAssistant</title>
<link rel="stylesheet" href="https://fonts.googleapis.com/css2?family=PT+Sans:wght@400;700&display=swap">
<style>
  :root {
    --page-bg: #f2f0f0;
    --header-bg: #ffffff;
    --nav-bg: #f3f1f1;
    --line: #e0dddd;
    --text-grey: #777777;
    --label-grey: #9a9a9a;
    --muted: #b5b5b5;
    --accent: #f4574a;
    --accent-hot: #ff6536;
    --white: #ffffff;
    --icon-grey: #a3a3a3;
  }
  * { box-sizing: border-box; margin: 0; padding: 0; }
  html, body { width: 1200px; height: 1000px; overflow: hidden; }
  body {
    position: relative;
    background: var(--page-bg);
    font-family: "PT Sans", Arial, sans-serif;
    color: var(--text-grey);
  }

  .site-header {
    position: absolute; left: 0; top: 0; width: 1200px; height: 116px;
    background: var(--header-bg);
  }
  .brand {
    position: absolute; left: 139px; top: 56px;
    font-size: 35px; font-weight: 400; letter-spacing: 1px; line-height: 40px;
    color: var(--text-grey);
  }
  .social { position: absolute; left: 987px; top: 65px; display: flex; gap: 5px; }
  .social span { width: 21px; height: 21px; background: var(--icon-grey); display: block; }
  .social svg { display: block; }

  .main-nav {
    position: absolute; left: 0; top: 116px; width: 1200px; height: 44px;
    background: var(--nav-bg);
    border-bottom: 1px solid var(--line);
  }
  .main-nav a {
    position: absolute; top: 13px; font-size: 14px; text-decoration: none; color: var(--text-grey);
  }
  .main-nav .current { left: 140px; color: var(--accent); }
  .main-nav .favs { left: 270px; }
  .search {
    position: absolute; left: 816px; top: 0; width: 170px; height: 43px;
    border-left: 1px solid var(--line);
    font-size: 11px; color: var(--muted); padding: 16px 0 0 14px;
  }
  .search svg { position: absolute; right: 15px; top: 13px; }
  .login {
    position: absolute; left: 986px; top: 0; width: 101px; height: 43px;
    border-left: 1px solid var(--line); border-right: 1px solid var(--line);
    font-size: 10px; color: var(--muted); padding: 17px 0 0 32px; letter-spacing: .3px;
  }
  .login svg { position: absolute; left: 76px; top: 19px; }

  .assistant-trigger {
    position: absolute; left: 601px; top: 227px; width: 112px; height: 112px;
    border-radius: 50%; background: var(--accent); color: var(--white);
    font-weight: 700; font-size: 18px; line-height: 24px; text-align: center;
    padding-top: 31px;
  }
  .close-btn { position: absolute; left: 709px; top: 220px; }

  .experience {
    position: absolute; width: 227px; height: 198px;
  }
  .experience .photo { width: 227px; height: 157px; }
  .experience .label {
    height: 41px; background: var(--white); color: var(--label-grey);
    font-size: 14px; text-align: center; line-height: 41px; letter-spacing: .3px;
  }
  .experience.selected .label { background: var(--accent-hot); color: var(--white); font-weight: 700; }

  .site-footer {
    position: absolute; left: 0; top: 965px; width: 1200px; height: 35px;
    background: var(--accent); color: var(--white); font-size: 12px; font-weight: 700;
  }
  .site-footer .lang { position: absolute; left: 140px; top: 11px; }
  .site-footer .plus { position: absolute; left: 1028px; top: 12px; }
  .site-footer svg { position: absolute; left: 1069px; top: 10px; }
</style>
</head>
<body>
  <header class="site-header">
    <div class="brand">VERMALO</div>
    <div class="social">
      <span></span><span></span><span></span>
      <span><svg width="21" height="21" viewBox="0 0 21 21"><rect width="21" height="21" fill="#a3a3a3"/><path d="M10.5 4.5v12M4.5 10.5h12" stroke="#fff" stroke-width="3"/></svg></span>
    </div>
  </header>

  <nav class="main-nav">
    <a class="current" href="#">MyAssistant</a>
    <a class="favs" href="#">MyFavourites</a>
    <div class="search">Search
      <svg width="17" height="17" viewBox="0 0 17 17"><circle cx="6.5" cy="6.5" r="5" fill="none" stroke="#a8a8a8" stroke-width="1.5"/><path d="M10.2 10.2l5.3 5.3" stroke="#a8a8a8" stroke-width="2.2"/></svg>
    </div>
    <div class="login">LOGIN
      <svg width="9" height="6" viewBox="0 0 9 6"><path d="M1 1l3.5 3.5L8 1" fill="none" stroke="#b0b0b0" stroke-width="1.3"/></svg>
    </div>
  </nav>

  <div class="assistant-trigger">I<br>WANT</div>
  <svg class="close-btn" width="26" height="26" viewBox="0 0 26 26"><circle cx="13" cy="13" r="11" fill="none" stroke="#6f6f6f" stroke-width="2"/><path d="M9.5 9.5l7 7M16.5 9.5l-7 7" stroke="#6f6f6f" stroke-width="2.2"/></svg>

  <div class="experience" style="left:140px;top:385px">
    <div class="photo" role="img" aria-label="Black and white close-up of a closed eye" style="background:linear-gradient(90deg,#bdbdbd,#e6e6e6 45%,#f4f4f4)"></div>
    <div class="label">DREAM</div>
  </div>
  <div class="experience" style="left:380px;top:385px">
    <div class="photo" role="img" aria-label="Carved stone sculpture on a building facade" style="background:radial-gradient(circle at 50% 55%,#c9c5bd,#a8a399 70%,#8c887f)"></div>
    <div class="label">ART</div>
  </div>
  <div class="experience" style="left:620px;top:385px">
    <div class="photo" role="img" aria-label="Cloudy grey-blue sky over the sea" style="background:linear-gradient(180deg,#9ea8bd,#b7bfcf 55%,#7e8ea5 90%,#5f7590)"></div>
    <div class="label">BREATH</div>
  </div>
  <div class="experience" style="left:860px;top:385px">
    <div class="photo" role="img" aria-label="Tiger resting against a rock wall" style="background:linear-gradient(180deg,#a8968c,#b19a88 55%,#c98a4e 80%,#b8773e)"></div>
    <div class="label">ANIMALS</div>
  </div>

  <div class="experience" style="left:140px;top:623px">
    <div class="photo" role="img" aria-label="Aircraft wing seen against a turquoise sky" style="background:linear-gradient(135deg,#58a9aa,#8fcbc6 55%,#cfe6e2)"></div>
    <div class="label">DREAM</div>
  </div>
  <div class="experience selected" style="left:380px;top:623px">
    <div class="photo" role="img" aria-label="Neon star sign against a blue evening sky" style="background:radial-gradient(circle at 50% 45%,#3aa0d8,#1e4d8a 45%,#1b3768)"></div>
    <div class="label">CELEBRITY</div>
  </div>
  <div class="experience" style="left:620px;top:623px">
    <div class="photo" role="img" aria-label="Red smiley balloon among party balloons" style="background:radial-gradient(circle at 60% 65%,#e8321c,#d42a14 45%,#9cc04a 75%,#c8d0d4)"></div>
    <div class="label">HAVE FUN</div>
  </div>
  <div class="experience" style="left:860px;top:623px">
    <div class="photo" role="img" aria-label="Illuminated castle with fireworks at night" style="background:radial-gradient(circle at 30% 80%,#8a3aa8,#2a1636 40%,#0d0b10)"></div>
    <div class="label">MAGIC</div>
  </div>

  <footer class="site-footer">
    <span class="lang">Language : English</span>
    <span class="plus">PLUS</span>
    <svg width="17" height="17" viewBox="0 0 17 17"><circle cx="8.5" cy="8.5" r="8.5" fill="#fff"/><path d="M4.5 6.5h8l-4 5z" fill="#f4574a"/></svg>
  </footer>
</body>
</html>
```